Website design needed for Renewable utilities company based in New Zealand.

Website design needed for Tarnwick Collective based in New Zealand.

Please see attached logo.

We sell solar panels, vertical axis wind turbines, atmospheric water generators and other related equipment for those who don't have access or don't want to depend on the government, city councils for their utilities (power and water).

We like metallic texture, dark grey and purple, red or blue colours. The design should go well with the attached logo.

Target Market(s)

The Eco conscious

Industry/Entity Type

Government

Logo Text

Tarnwick Horizon

Requirements
Must have
• Must Have:
- Metallic finish is a must.
- Design should fit around the attached logo well.
Nice to have
• Sharpe design prefred rather than rounded edges

```html
<!DOCTYPE html>
<html lang="en">
<head>
<meta charset="utf-8">
<title>Tarnwick Horizon</title>
<link rel="stylesheet" href="https://fonts.googleapis.com/css2?family=Arimo:wght@400;700&family=Oswald:wght@400;500&display=swap">
<style>
:root{
  --steel-light:#e4e4e4;
  --steel-mid:#a9a9a9;
  --steel-dark:#3a3a3a;
  --ink:#111;
  --body:#444;
  --muted:#8a8a8a;
  --white:#fff;
  --red:#e0101a;
  --blue:#1a8ad4;
  --link:#1a6fb8;
  --sun:#f2e600;
  --wind:#17a336;
  --water:#1d7fe0;
  --navy:#0c2a78;
  --panel-line:#cfcfcf;
}
*{box-sizing:border-box;margin:0;padding:0}
html,body{width:752px;height:1200px;overflow:hidden}
body{
  position:relative;font-family:Arimo,Arial,sans-serif;color:var(--ink);
  background:
    repeating-linear-gradient(90deg,rgba(255,255,255,.06) 0 1px,rgba(0,0,0,.05) 1px 3px,transparent 3px 5px),
    linear-gradient(90deg,#5a5a5a,#9a9a9a 30%,#7c7c7c 55%,#a5a5a5 80%,#5e5e5e);
}
.abs{position:absolute}
/* header */
.site-header{left:0;top:0;width:752px;height:88px;
  background:repeating-linear-gradient(90deg,rgba(0,0,0,.03) 0 1px,transparent 1px 4px),linear-gradient(180deg,#f2f2f2,#d6d6d6);
  border-bottom:1px solid #8a8a8a}
.brand{left:44px;top:10px;width:130px;text-align:center}
.brand-dot{display:block;width:44px;height:44px;border-radius:50%;background:var(--link);margin:0 auto 6px}
.brand-name{font-size:15px;font-weight:700;color:var(--link);white-space:nowrap}
.contact-box{left:430px;top:10px;width:161px;height:38px;background:var(--white);border:1px solid #c8c8c8;font-size:8.5px;padding:5px 6px;line-height:14px}
.contact-box .val{position:absolute;left:75px;color:var(--link)}
.contact-box .val.phone{font-weight:700}
.contact-box .val.mail{left:66px;text-decoration:underline}
.contact-box svg{vertical-align:-2px;margin-right:4px}
.cta{left:594px;top:10px;width:120px;height:38px;background:#161616;border:1px solid #555;text-align:center;font-family:Arimo,sans-serif}
.cta b{display:block;color:var(--red);font-size:11.5px;margin-top:4px;letter-spacing:.5px}
.cta span{display:block;color:#ddd;font-size:7.5px;line-height:9px;letter-spacing:.4px}
.main-nav{left:190px;top:59px;width:525px;height:23px;background:linear-gradient(180deg,#5a5a5a,#262626);border:1px solid #1a1a1a;display:flex;font-size:8px;color:var(--white)}
.main-nav a{color:inherit;text-decoration:none;display:flex;align-items:center;justify-content:center;border-right:1px solid #777;height:100%}
.main-nav a.home{width:34px;background:#2a2a2a;border-bottom:2px solid var(--blue)}
/* content panel */
.content{left:38px;top:105px;width:677px;height:910px;background:var(--white)}
.hero{left:43px;top:111px;width:666px;height:264px;background:linear-gradient(180deg,#7fb1df 0%,#b8d3ea 35%,#6a5a50 60%,#3c3c44 100%)}
.hero-tag{left:43px;top:111px;width:128px;height:54px;background:var(--blue);color:var(--white);font-family:Oswald,sans-serif;font-size:14px;line-height:19px;padding:6px 8px}
.hero-tag u{text-decoration:underline}
.hero-copy{left:429px;top:137px;width:280px;height:145px;background:rgba(255,255,255,.85);padding:6px 12px}
.hero-copy h1{font-family:Oswald,sans-serif;font-weight:400;font-size:34px;line-height:40px;color:var(--ink)}
.hero-copy .accent{display:block;color:var(--red);font-size:25px;line-height:32px}
.hero-copy .line{display:block;font-size:25px;line-height:32px}
.hero-copy .strap{display:inline-block;background:var(--red);color:var(--white);font-family:Oswald,sans-serif;font-size:10px;letter-spacing:1.5px;padding:1px 5px;margin-top:2px}
.hero-arrow{top:225px}
.hero-bar{left:43px;top:357px;width:666px;height:18px;background:rgba(0,0,0,.55)}
.dots{left:366px;top:364px;display:flex;gap:4px}
.dots i{width:4px;height:4px;border-radius:50%;background:var(--white)}
.dots i:first-child{background:var(--blue)}
.hero-shadow{left:43px;top:375px;width:666px;height:14px;background:radial-gradient(ellipse at top,rgba(0,0,0,.25),transparent 70%)}
/* features */
.feature{top:402px;width:214px;height:112px;border:1px solid #111;padding:22px 30px;color:var(--white);
  background:repeating-linear-gradient(90deg,rgba(255,255,255,.05) 0 1px,transparent 1px 4px),linear-gradient(160deg,#6a6a6a,#2d2d2d 60%,#444)}
.feature h2{font-family:Arimo,sans-serif;font-size:16px;font-weight:700;line-height:20px}
.feature p{font-size:10px;line-height:13px;margin-top:4px}
.feature .corner{position:absolute;right:0;bottom:0}
.sun h2{color:var(--sun)}.wind h2{color:var(--wind)}.water h2{color:var(--water)}
/* sections */
.section{left:45px;width:664px;border:1px solid var(--panel-line);background:var(--white)}
.section-head{height:22px;background:linear-gradient(180deg,#555,#1e1e1e);color:var(--white);font-size:13px;display:flex;align-items:center;padding-left:6px;letter-spacing:.3px}
.section-head i{width:13px;height:13px;border-radius:50%;background:#ddd;margin-right:6px}
.product{position:absolute;top:36px;width:320px}
.product .shot{position:absolute;left:10px;top:0;width:100px;height:90px}
.product .text{position:absolute;left:133px;top:0;width:180px}
.product h3{font-size:9px;font-weight:700;line-height:11px}
.product p{font-size:6.6px;line-height:8.6px;color:var(--body);margin-top:7px}
.btn{display:inline-block;background:#111;color:var(--white);font-size:7px;padding:2px 5px;margin-top:6px}
.divider{position:absolute;left:331px;top:32px;width:1px;height:110px;background:#ddd}
.brands{display:flex;align-items:center;height:80px;background:#f4f4f4}
.brands .nav{width:24px;height:80px;display:flex;align-items:center;justify-content:center;background:#e8e8e8}
.brand-row{flex:1;height:80px;background:var(--white);display:flex;justify-content:space-around;align-items:center;font-weight:700}
.view-link{position:absolute;font-size:8px;color:var(--link);text-decoration:underline}
.testimonial{position:relative;height:134px;background:linear-gradient(90deg,#eee,#e6e6e6)}
.portrait{position:absolute;left:13px;top:10px;width:100px;height:112px;background:linear-gradient(160deg,#a6a39a,#7a6d5c 55%,#b23040);border:4px solid var(--white);box-shadow:0 0 3px rgba(0,0,0,.3)}
.quote{position:absolute;left:122px;top:8px;width:530px}
.quote .mark{font-family:Oswald,sans-serif;font-size:38px;color:#bbb;line-height:30px}
.quote p{font-size:8px;line-height:13px;color:var(--muted);margin-top:4px}
.quote cite{display:block;font-style:normal;font-weight:700;font-size:7.5px;color:#666;margin-top:10px;letter-spacing:.3px}
/* footer */
.site-footer{left:0;top:1022px;width:752px;height:170px;color:var(--white);
  background:repeating-linear-gradient(90deg,rgba(255,255,255,.04) 0 1px,transparent 1px 4px),linear-gradient(180deg,#4a4a4a,#1a1a1a 70%,#2a2a2a)}
.col h4{font-size:17px;font-weight:400;letter-spacing:1.5px;margin-bottom:16px}
.col a{display:block;color:var(--white);font-size:7.5px;line-height:11.5px;text-decoration:underline;letter-spacing:.5px}
.foot-brand{left:300px;top:6px;width:160px;text-align:center;font-size:6.5px;line-height:9px}
.foot-brand .dot{display:block;width:30px;height:30px;border-radius:50%;background:var(--link);margin:0 auto 3px}
.foot-brand .name{font-size:11px;font-weight:700;color:var(--link);margin-bottom:3px}
.foot-brand u{color:var(--white)}
.follow{font-size:10px;letter-spacing:.5px;margin-top:8px}
.socials{display:flex;gap:5px;justify-content:center;margin-top:5px}
.socials i{width:20px;height:20px;border-radius:50%;background:#e8e8e8}
.join h4{font-size:16px;margin-bottom:3px}
.join small{font-size:7px;display:block;margin-bottom:3px}
.join .field{width:210px;height:20px;background:var(--white);color:#ccc;font-size:9px;padding:4px 5px}
.join .sub{display:inline-block;background:#111;font-size:8px;font-weight:700;padding:5px 8px;margin-top:8px}
.copyright{left:0;top:1188px;width:752px;height:12px;background:#0d0d0d;color:#ccc;font-size:5.5px;padding:3px 44px;letter-spacing:.3px}
</style>
</head>
<body>

<header class="site-header abs">
  <div class="brand abs"><span class="brand-dot"></span><span class="brand-name">Tarnwick Horizon</span></div>
  <div class="contact-box abs">
    <div><svg width="9" height="9" viewBox="0 0 10 10"><path d="M2 1 L4 1 L4.5 3.5 L3 4.5 Q4 6.5 5.5 7 L6.5 5.5 L9 6 L9 8 Q5 9.5 1 4 Z" fill="#1b3b7a"/></svg>Call us:<span class="val phone">+64 (0)9 555 0142</span></div>
    <div><svg width="9" height="7" viewBox="0 0 10 7"><rect x=".5" y=".5" width="9" height="6" fill="none" stroke="#1b3b7a"/><path d="M.5 .5 L5 4 L9.5 .5" fill="none" stroke="#1b3b7a"/></svg>E-mail us:<span class="val mail">sales@tarnwick.co.nz</span></div>
  </div>
  <div class="cta abs"><b>CONTROL NOW</b><span>YOUR ENERGY BILL</span><span>AND SAVE MONEY!</span></div>
  <nav class="main-nav abs">
    <a class="home" href="#" aria-label="Home"><svg width="9" height="8" viewBox="0 0 10 9"><path d="M5 0 L10 4.5 H8.5 V9 H6 V6 H4 V9 H1.5 V4.5 H0 Z" fill="#fff"/></svg></a>
    <a href="#" style="width:96px">For Homes</a>
    <a href="#" style="width:108px">Bussiness &amp; Government</a>
    <a href="#" style="width:100px">Why Tarnwick Horizon</a>
    <a href="#" style="width:81px">Products &amp; Services</a>
    <a href="#" style="width:62px">Company</a>
    <a href="#" style="width:42px;border:0">Contact</a>
  </nav>
</header>

<div class="content abs"></div>

<section class="hero abs" role="img" aria-label="Photo of a brick house roof covered with solar panels under a blue sky, with trees"></section>
<div class="hero-tag abs"><u>VIEW NOW</u><br><u>OUR SOLAR PANELS</u> ▸</div>
<div class="hero-copy abs">
  <h1>LIKE<span class="accent">NOTHING ELSE</span><span class="line">ON YOUR HOME’S ROOF</span></h1>
  <span class="strap">MORE ENERGY FOR YOUR FAMILLY!</span>
</div>
<svg class="hero-arrow abs" style="left:51px" width="14" height="30" viewBox="0 0 14 30"><path d="M12 1 L2 15 L12 29" fill="none" stroke="#222" stroke-width="2"/></svg>
<svg class="hero-arrow abs" style="left:686px" width="14" height="30" viewBox="0 0 14 30"><path d="M2 1 L12 15 L2 29" fill="none" stroke="#222" stroke-width="2"/></svg>
<div class="hero-bar abs"></div>
<div class="dots abs"><i></i><i></i><i></i></div>
<div class="hero-shadow abs"></div>

<div class="feature sun abs" style="left:44px"><h2>POWER<br>OF THE SUN</h2><p>SWITCH YOUR ELECTRICITY<br>TO SOLAR POWER</p><svg class="corner" width="14" height="14"><path d="M14 0 V14 H0 Z" fill="var(--navy)"/></svg></div>
<div class="feature wind abs" style="left:269px"><h2>POWER<br>OF THE WIND</h2><p>USE THE WIND POWER TO<br>REDUCE YOUR ENERGY BILL</p><svg class="corner" width="14" height="14"><path d="M14 0 V14 H0 Z" fill="var(--navy)"/></svg></div>
<div class="feature water abs" style="left:494px"><h2>ULTRA PURE<br>DRINKING WATER</h2><p>THE BEST WATER TO DRINK<br>FOR YOUR FAMILLY’S HEALTH</p><svg class="corner" width="14" height="14"><path d="M14 0 V14 H0 Z" fill="var(--navy)"/></svg></div>

<section class="section abs" style="top:538px;height:157px">
  <div class="section-head"><i></i>FEAUTURED PRODUCTS</div>
  <div class="product" style="left:0">
    <div class="shot" style="background:linear-gradient(135deg,#2a2a2a,#0a0a0a)" role="img" aria-label="Black solar panel product photo"></div>
    <div class="text">
      <h3>LOREM IPSUM DOLOR SIT AMET<br>CONSECTETUR ADIPISICING ELIT</h3>
      <p>Lorem ipsum dolor sit amet, consectetur adipisicing elit, sed do eiusmod tempor incididunt ut labore et dolore magna aliqua. Ut enim ad minim veniam, quis nostrud exercitation ullamco laboris nisi ut aliquip ex ea commodo consequat.</p>
      <span class="btn">Read more...</span>
    </div>
  </div>
  <div class="divider"></div>
  <div class="product" style="left:336px">
    <div class="shot" style="background:linear-gradient(180deg,#2e6fb4,#1d4f8e)" role="img" aria-label="Vertical axis wind turbine against a blue sky"></div>
    <div class="text">
      <h3>LOREM IPSUM DOLOR SIT AMET<br>CONSECTETUR ADIPISICING ELIT</h3>
      <p>Lorem ipsum dolor sit amet, consectetur adipisicing elit, sed do eiusmod tempor incididunt ut labore et dolore magna aliqua. Ut enim ad minim veniam, quis nostrud exercitation ullamco laboris nisi ut aliquip ex ea commodo consequat.</p>
      <span class="btn">Read more...</span>
    </div>
  </div>
</section>

<section class="section abs" style="top:718px;height:103px">
  <div class="section-head"><i></i>BRANDS WE SELL</div>
  <div class="brands">
    <div class="nav"><svg width="8" height="16"><path d="M7 1 L1 8 L7 15" fill="none" stroke="#333" stroke-width="1.3"/></svg></div>
    <div class="brand-row" style="font-size:15px">
      <span style="color:#a50034">Lumora</span>
      <span style="color:#333">Brightfield</span>
      <span style="color:#b0101a">Kestrel Cells</span>
      <span style="color:#00287a">Halden Power</span>
      <span style="color:#e0101a">Vexa</span>
      <span style="color:#d41b3c">Sorell</span>
    </div>
    <div class="nav"><svg width="8" height="16"><path d="M1 1 L7 8 L1 15" fill="none" stroke="#333" stroke-width="1.3"/></svg></div>
  </div>
  <span class="view-link" style="right:30px;top:90px">View All</span>
</section>

<section class="section abs" style="top:848px;height:157px">
  <div class="section-head"><i></i>TESTIMONIALS</div>
  <div class="testimonial">
    <div class="portrait" role="img" aria-label="Photo of a happy customer and family member outdoors"></div>
    <div class="quote">
      <div class="mark">“</div>
      <p>Lorem ipsum dolor sit amet, consectetur adipisicing elit, sed do eiusmod tempor incididunt ut labore et dolore magna aliqua. Ut enim ad minim veniam, quis nostrud exercitation ullamco laboris nisi ut aliquip ex ea commodo consequat. Duis aute irure dolor in reprehenderit in voluptate velit esse cillum dolore eu fugiat nulla pariatur. Excepteur sint occaecat cupidatat non proident, sunt in culpa qui officia deserunt mollit anim id est laborum.</p>
      <cite>Ewan Carlisle, Wellington, New Zealand</cite>
    </div>
  </div>
  <span class="view-link" style="right:14px;top:144px">View Testimonials</span>
</section>

<footer class="site-footer abs">
  <div class="col abs" style="left:42px;top:58px">
    <h4>PRODUCTS</h4>
    <a href="#">For Homes</a><a href="#">Bussiness &amp; Government</a><a href="#">Solar Panels</a><a href="#">Vertical Axis Wind Turbines,</a><a href="#">Atmospheric Water Generators</a>
  </div>
  <div class="col abs" style="left:198px;top:58px">
    <h4>INFO</h4>
    <a href="#">Why Tarnwick Horizon</a><a href="#">About us</a><a href="#">Contact</a><a href="#">Terms</a><a href="#">Help</a>
  </div>
  <div class="foot-brand abs">
    <span class="dot"></span>
    <div class="name">Tarnwick Horizon</div>
    Kerrow St, Hamilton, 3204, WAIKATO, NZ<br>+64 (0)9 555 0142<br><u>sales@tarnwick.co.nz</u>
    <div class="follow">FOLLOW US</div>
    <div class="socials" aria-label="Social links"><i></i><i></i><i></i><i></i><i></i></div>
  </div>
  <div class="join col abs" style="left:489px;top:56px">
    <h4>JOIN NOW</h4>
    <small>Sign up for deals, news, and giveaways:</small>
    <div class="field">Email Address</div>
    <span class="sub">SUBSCRIBE</span>
  </div>
</footer>
<div class="copyright abs">©2013 TARNWICK.CO.NZ. ALL RIGHTS RESERVED. SITEMAP</div>

</body>
</html>
```